Prestige Car Bodyshop Business Card

We are a car bodyshop based in the UK. Our customer base is mainly prestige high-value vehicles. I am looking for a classy and stylish business card design for my staff to give out to customers, with their direct email and phone number, as well as our main email and phone number with address details

I am also looking to have a general business card design with just our main company address and contact details, but also have a space to add a manufacturer approval logo (i.e Velmora, Orek, Tovalo etc... logo) in the corner somewhere.

I do not particularly want any outlines or pictures of cars on the card, I would just like a quality high-end look.

Please feel free to get in touch if you have any questions or queries?

Many Thanks

Malcolm

Target Market(s)

Prestige vehicle owners

Industry/Entity Type

Automotive

Contact Information for Business Card

I am looking for a classy and stylish business card design for my staff to give out to customers, with their direct email and phone number, as well as our main email and phone number with address details

Font styles to use
Sans Serif

Colors

Designer to choose colors to be used in the design.

Requirements
Nice to have
• I do not particularly want any outlines or pictures of cars on the card, I would just like a quality high-end look.

```html
<!DOCTYPE html>
<html lang="en">
<head>
<meta charset="utf-8">
<title>RK Halden Business Cards</title>
<link href="https://fonts.googleapis.com/css2?family=Source+Sans+3:wght@400;600&family=Pinyon+Script&display=swap" rel="stylesheet">
<style>
  :root {
    --page: #e6e7e9;
    --card: #ffffff;
    --brand-blue: #1f76bd;
    --brand-blue-deep: #15599a;
    --brand-blue-light: #2a8bd6;
    --accent-orange: #f0592a;
    --text-grey: #8a8d90;
    --text-dark: #55585b;
    --badge-fill: #eef2f6;
    --badge-edge: #c9d3dd;
  }
  * { box-sizing: border-box; margin: 0; padding: 0; }
  html, body { width: 1200px; height: 966px; overflow: hidden; }
  body {
    background: var(--page);
    font-family: "Source Sans 3", sans-serif;
    display: flex;
    flex-direction: column;
    align-items: center;
    justify-content: center;
    gap: 40px;
  }
  .card {
    position: relative;
    width: 760px;
    height: 434px;
    background: var(--card);
    overflow: hidden;
    box-shadow: 0 6px 18px rgba(0,0,0,0.12);
  }
  .card__waves { position: absolute; inset: 0; width: 100%; height: 100%; }
  .brand-name {
    position: absolute;
    left: 60px;
    top: 62px;
    font-weight: 600;
    font-size: 42px;
    letter-spacing: 0.5px;
    color: var(--brand-blue);
    line-height: 1;
  }
  .approval-badge {
    position: absolute;
    right: 60px;
    top: 46px;
    width: 84px;
    height: 84px;
    border-radius: 8px;
    background: var(--badge-fill);
    border: 1px solid var(--badge-edge);
  }
  .slogan {
    position: absolute;
    right: 64px;
    top: 150px;
    font-family: "Pinyon Script", cursive;
    font-size: 40px;
    color: var(--brand-blue-light);
    line-height: 1.2;
  }
  .contact {
    position: absolute;
    right: 56px;
    top: 44px;
    text-align: right;
  }
  .contact__name {
    font-weight: 600;
    font-size: 26px;
    color: var(--brand-blue);
    letter-spacing: 0.5px;
    line-height: 1.05;
  }
  .contact__title {
    font-size: 17px;
    color: var(--text-grey);
    letter-spacing: 3px;
    line-height: 1.2;
    margin-bottom: 10px;
  }
  .contact__line {
    display: flex;
    justify-content: flex-end;
    align-items: center;
    gap: 10px;
    font-size: 18px;
    line-height: 26px;
    color: var(--text-dark);
  }
  .icon { width: 15px; height: 15px; fill: var(--brand-blue); flex: none; }
  .company-details {
    position: absolute;
    left: 36px;
    bottom: 22px;
    color: #ffffff;
    font-size: 18px;
    line-height: 28px;
  }
  .company-details__row { display: flex; align-items: center; gap: 10px; }
  .company-details__row + .company-details__row { gap: 22px; }
  .company-details .icon { fill: #ffffff; }
  .company-details__item { display: flex; align-items: center; gap: 8px; }
</style>
</head>
<body>

  <section class="card card--front">
    <svg class="card__waves" viewBox="0 0 760 434" preserveAspectRatio="none" aria-hidden="true">
      <defs>
        <linearGradient id="bandFront" x1="0" y1="0" x2="1" y2="0">
          <stop offset="0" stop-color="#2a8bd6"/>
          <stop offset="1" stop-color="#15599a"/>
        </linearGradient>
      </defs>
      <path d="M360 274 C500 266 640 252 760 230 L760 238 C640 260 500 270 360 274 Z" fill="#f0592a"/>
      <path d="M0 418 C120 350 330 306 760 252 L760 434 L0 434 Z" fill="url(#bandFront)"/>
      <path d="M0 432 C140 366 360 322 760 270" fill="none" stroke="#ffffff" stroke-width="5"/>
    </svg>
    <div class="brand-name">RK HALDEN</div>
    <div class="approval-badge" role="img" aria-label="Space for manufacturer approval badge"></div>
    <div class="slogan">We Deliver!</div>
  </section>

  <section class="card card--back">
    <svg class="card__waves" viewBox="0 0 760 434" preserveAspectRatio="none" aria-hidden="true">
      <defs>
        <linearGradient id="bandBack" x1="0" y1="0" x2="1" y2="0">
          <stop offset="0" stop-color="#2a8bd6"/>
          <stop offset="1" stop-color="#15599a"/>
        </linearGradient>
      </defs>
      <path d="M360 244 C500 236 640 222 760 202 L760 210 C640 230 500 240 360 244 Z" fill="#f0592a"/>
      <path d="M0 330 C130 276 340 244 760 222 L760 434 L0 434 Z" fill="url(#bandBack)"/>
      <path d="M0 348 C150 294 360 262 760 240" fill="none" stroke="#ffffff" stroke-width="5"/>
    </svg>
    <div class="brand-name">RK HALDEN</div>
    <div class="contact">
      <div class="contact__name">PERSONS NAME</div>
      <div class="contact__title">PERSONS TITLE</div>
      <div class="contact__line">07700 900418
        <svg class="icon" viewBox="0 0 24 24"><path d="M6.6 10.8a15.1 15.1 0 0 0 6.6 6.6l2.2-2.2c.3-.3.7-.4 1-.2 1.1.4 2.3.6 3.6.6.6 0 1 .4 1 1V20c0 .6-.4 1-1 1A17 17 0 0 1 3 4c0-.6.4-1 1-1h3.5c.6 0 1 .4 1 1 0 1.3.2 2.5.6 3.6.1.3 0 .7-.2 1z"/></svg>
      </div>
      <div class="contact__line">name@rkhalden.co.uk
        <svg class="icon" viewBox="0 0 24 24"><path d="M2 5h20v14H2zm2 2v.4l8 5.2 8-5.2V7zm0 2.8V17h16V9.8l-8 5.2z"/></svg>
      </div>
    </div>
    <div class="company-details">
      <div class="company-details__row">
        <svg class="icon" viewBox="0 0 18 24"><path d="M9 0a9 9 0 0 0-9 9c0 6.8 9 15 9 15s9-8.2 9-15a9 9 0 0 0-9-9zm0 12.5A3.5 3.5 0 1 1 9 5.5a3.5 3.5 0 0 1 0 7z"/></svg>
        14 Kestrel Park, Harrowgate Lane, Leeds LS12 4QT
      </div>
      <div class="company-details__row">
        <span class="company-details__item">
          <svg class="icon" viewBox="0 0 24 24"><path d="M6.6 10.8a15.1 15.1 0 0 0 6.6 6.6l2.2-2.2c.3-.3.7-.4 1-.2 1.1.4 2.3.6 3.6.6.6 0 1 .4 1 1V20c0 .6-.4 1-1 1A17 17 0 0 1 3 4c0-.6.4-1 1-1h3.5c.6 0 1 .4 1 1 0 1.3.2 2.5.6 3.6.1.3 0 .7-.2 1z"/></svg>
          0113 496 0732
        </span>
        <span class="company-details__item">
          <svg class="icon" viewBox="0 0 24 24"><path d="M2 5h20v14H2zm2 2v.4l8 5.2 8-5.2V7zm0 2.8V17h16V9.8l-8 5.2z"/></svg>
          info@rkhalden.co.uk
        </span>
        <span class="company-details__item">
          <svg class="icon" viewBox="0 0 24 24"><path d="M12 2a10 10 0 1 0 0 20 10 10 0 0 0 0-20zm6.9 6h-3a15.7 15.7 0 0 0-1.3-3.6A8 8 0 0 1 18.9 8zM12 4c.8 1.2 1.5 2.5 1.9 4h-3.8c.4-1.5 1.1-2.8 1.9-4zM4.3 14a8 8 0 0 1 0-4h3.4a16 16 0 0 0 0 4zm.8 2h3c.3 1.3.8 2.5 1.3 3.6A8 8 0 0 1 5.1 16zm3-8h-3a8 8 0 0 1 4.3-3.6C8.9 5.5 8.4 6.7 8.1 8zM12 20c-.8-1.2-1.5-2.5-1.9-4h3.8c-.4 1.5-1.1 2.8-1.9 4zm2.3-6H9.7a14.7 14.7 0 0 1 0-4h4.6a14.7 14.7 0 0 1 0 4zm.3 5.6c.5-1.1 1-2.3 1.3-3.6h3a8 8 0 0 1-4.3 3.6zM16.3 14a16 16 0 0 0 0-4h3.4a8 8 0 0 1 0 4z"/></svg>
          www.rkhalden.co.uk
        </span>
      </div>
    </div>
  </section>

</body>
</html>
```